Redesign Of Hotel Coupon/Voucher 8.5 x 11

I would like to redesign my voucher.

Please provide me a color flyer design but one that would be easy on printing costs...for example printing from home computer/printer.

I would like to see some color designs...maybe some black and white and also full graphics and even basic like the plum rook voucher I provided as a sample. The 2 night hotel stay is the voucher I need to redesign...

Target Market(s)

Consumers

Industry/Entity Type

Hotel

Requirements
Must have
• exact text in current designs---look official, credible and trust worthy
Nice to have
• I would like to redesign my voucher.
• Please provide me a color flyer design but one that would be easy on printing costs...for example printing from home computer/printer.
• I would like to see some color designs...maybe some black and white and also full graphics and even basic like the plum rook voucher I provided as a sample. The 2 night hotel stay is the voucher I need to redesign...
Should not have

```html
<!DOCTYPE html>
<html lang="en">
<head>
<meta charset="utf-8">
<title>2 Night Hotel Stay Certificate</title>
<link href="https://fonts.googleapis.com/css2?family=Montserrat:wght@400;500;600;700;800&family=Arimo:wght@400;700&display=swap" rel="stylesheet">
<style>
:root{
  --blue:#2b3f9c;
  --navy:#1a2859;
  --panel:#e7e7ea;
  --ink:#1c1c1c;
  --red:#e4342c;
  --page:#ffffff;
  --bg:#d9d6d2;
}
*{box-sizing:border-box;margin:0;padding:0}
html,body{width:1200px;height:1000px;overflow:hidden;background:var(--bg)}
body{position:relative;font-family:'Montserrat',sans-serif;color:var(--ink)}
.flyer{position:absolute;left:222px;top:14px;width:788px;height:1012px;background:var(--page);transform:scale(.96);transform-origin:0 0;box-shadow:0 4px 18px rgba(0,0,0,.25);overflow:hidden}
.hero-photo{position:absolute;left:0;top:0;width:788px;height:300px;background:linear-gradient(180deg,#c9d2dc 0%,#b7a48a 45%,#6b5a48 75%,#e9e9ea 100%)}
.hero-fade{position:absolute;left:0;top:230px;width:788px;height:75px;background:linear-gradient(180deg,rgba(255,255,255,0),#fff)}
.compliments{position:absolute;left:563px;top:0;width:214px;height:218px;background:var(--blue);border:4px solid #fff;border-top:none;color:#fff;text-align:center;font-weight:700}
.compliments h2{font-size:14.5px;line-height:18px;margin-top:32px;letter-spacing:.3px}
.compliments p{font-size:12px;line-height:21px;font-weight:600}
.compliments .contact{margin-top:36px}
.title{position:absolute;left:0;width:788px;top:238px;text-align:center;font-family:'Arimo',sans-serif;font-weight:700;font-size:42px;color:#fff;text-shadow:2px 2px 4px rgba(0,0,0,.85),0 0 2px #000;letter-spacing:.5px}
.destinations{position:absolute;left:30px;top:302px;width:728px;height:90px;background:var(--panel);padding:4px 6px;font-family:'Arimo',sans-serif;font-weight:700;font-size:9.3px;line-height:14.2px}
.terms-tab{position:absolute;left:0;top:397px;height:27px;width:212px;background:var(--blue);clip-path:polygon(0 0,100% 0,93% 100%,0 100%);color:#fff;font-weight:600;font-size:13.5px;line-height:27px;padding-left:36px}
.terms-rule{position:absolute;left:0;top:424px;width:6px;height:6px;background:var(--navy)}
.terms{position:absolute;left:30px;top:432px;width:728px;height:232px;background:var(--panel);padding:6px 5px;font-size:8.05px;line-height:11.55px;text-align:justify}
.lower{position:absolute;left:0;top:674px;width:788px;height:338px;background:var(--panel)}
.form-col{position:absolute;top:0}
.billing{left:36px;width:224px}
.payment{left:527px;width:230px}
.form-col h3{font-size:13.5px;font-weight:700;margin-top:9px;margin-bottom:6px}
.row{display:flex;align-items:flex-end;height:17.8px;font-size:10.8px;font-weight:600}
.row .label{white-space:nowrap}
.row .line{flex:1;border-bottom:1px solid #333;margin-left:2px;height:11px}
.billing .row .line{margin-left:0;flex:none;width:171px;position:absolute;left:53px}
.billing .row{position:relative}
.redeem{position:absolute;left:272px;top:0;width:244px;height:338px;background:var(--navy);clip-path:polygon(0 0,8% 0,50% 0,92% 0,100% 0,100% 0,100% 100%,0 100%,0 0)}
.redeem-inner{position:absolute;left:290px;top:25px;width:208px;height:313px;background:var(--blue);color:#fff}
.redeem-notch{position:absolute;top:0;height:25px;width:20px;background:var(--panel)}
.notch-l{left:272px;clip-path:polygon(0 0,100% 0,0 100%)}
.notch-r{left:496px;clip-path:polygon(0 0,100% 0,100% 100%)}
.redeem-inner .intro{font-size:10.4px;line-height:13px;text-align:center;padding:17px 8px 0;font-weight:500}
.redeem-inner h4{font-size:12.5px;font-weight:700;margin:20px 0 4px 8px}
.redeem-inner .step{font-size:8.9px;font-weight:700;margin-left:8px;line-height:12px}
.redeem-inner .link{font-size:9px;text-align:center;text-decoration:underline;margin:5px 0 6px;font-weight:500}
.redeem-inner .addr{font-size:8.2px;line-height:9.8px;text-align:center;margin-top:7px;font-weight:500}
.redeem-inner .ids{font-size:12px;font-weight:700;margin:14px 0 0 8px;line-height:17px}
.ids .exp{color:var(--red);font-weight:600}
.methods{display:grid;grid-template-columns:68px 120px;row-gap:6px;margin:10px 0 8px 24px;font-size:10.8px;font-weight:600}
.methods span{display:flex;align-items:center}
.methods i{width:14px;height:14px;border:1px solid #333;background:#fff;margin-right:4px;display:inline-block}
.payment .row .line{flex:none;width:130px;margin-left:auto}
.exp-row .slot{border-bottom:1px solid #333;width:24px;height:11px;margin:0 8px 0 6px}
.exp-row .slot2{border-bottom:1px solid #333;width:70px;height:11px;margin-left:6px}
.agree{font-size:10.8px;font-weight:600;margin-top:12px}
.notes{font-family:'Arimo',sans-serif;font-size:7.4px;line-height:10px;margin-top:10px}
.notes p+p{margin-top:4px}
.code{font-family:'Arimo',sans-serif;font-size:7px;font-weight:700;text-align:right;margin-top:6px;padding-right:8px}
</style>
</head>
<body>
<main class="flyer">
  <div class="hero-photo" role="img" aria-label="Photo of a hotel room window table with coffee cups and juice overlooking city skyscrapers at sunset"></div>
  <div class="hero-fade"></div>
  <section class="compliments">
    <h2>THE CERTIFICATE IS<br>COMPLIMENTS OF:</h2>
    <div class="contact"><p>NAME</p><p>PHONE NUMBER</p><p>E-MAIL ADDRESS</p></div>
  </section>
  <h1 class="title">2 Night Hotel Stay</h1>

  <section class="destinations">
    Destinations Available: Anaheim, CA--Atlanta, GA--Atlantic City, NJ--Branson, MO--Cancun, MX--Charleston, SC--Coeur d' Alene, ID--Daytona Beach, FL--Destin, FL--Ft. Lauderdale, FL--Ft. Meyers, FL--Gatlinburg, TN--Hilton Head, SC--Honolulu, HI--Kissimmee, FL--Lake Tahoe, CA--Las Vegas, NV--Myrtle Beach, SC--Niagara Falls/Buffalo Area, NY--Orlando, FL--Ormond Beach, FL--Palm Springs, CA--Pigeon Forge, TN--St. Petersburg, FL--San Antonio, TX--San Diego, CA--San Francisco, CA--Sedona, AZ--Sonoma Wine Country, CA--St. George, UT--Tampa, FL--Williamsburg, VA--Wisconsin Dells, WI--Tallahassee, FL--Augusta, GA--Columbia, SC--New York, NY--Florence, SC--Washington, D.C.--Chicago, IL--Salt Lake City, UT--Hollywood, CA-Dayton, OH--Tucson, AZ--Niagra Falls, ON/CAN--Seattle, WA--Portland, OR--Antioch, CA--San Mateo, CA--Brunswick, GA--Nashville, TN
  </section>

  <div class="terms-tab">TERMS &amp; CONDITIONS</div>
  <section class="terms">
    This certificate will be considered void if bartered or purchased for legal tender by the recipient. This certificate is valid for a reservation request form offering 2adults 21 years of age and older plus up to 2 children under the age of 18, 2 nights of hotel accommodations in the city of their choice of available cities. The costto activate this certificate to receive the reservation request form is just a one-time non-refundable $14.95 processing fee. The cost upon requesting reservationsis just a tax &amp; fee deposit of $33 per night. Taxes &amp; fees usually range from $12-$33 per night depending on when and where you travel to. If the taxes &amp; feesare less than the $33 per night the difference will be refunded after travel is completed. 30 days advance reservation notice is required. In order to guaranteethat you will show up to your booked reservation you will be required to pay a REFUNDABLE $50 "Reservation Guarantee Deposit". If you send in your traveldates, etc and you do not end up traveling then the reservation guarantee deposit will not be refundable. 7 days before and after holidays and conventions arenot available. This offer is valid 7 days a week subject to availability. Friday and Saturday nights will require a surcharge of $20 per night. A $5 per person pernight surcharge is enforced for each child up to 2 children under the age of 18. This offer is not valid for group travel. The recipient of this certificate isresponsible for all expenses including but not limited to: transfers, food, gratuities, all pertinent fees, taxes, hotel surcharges, resort fees and any othermiscellaneous expenses. If you activate this certificate online you will be able to instantly print your reservation request form. If you cannot print your ownreservation request form we will mail it to you. You should receive it in the mail within 14 days. This certificate cannot be combined with any other promotionalvacation offer. The expiration date on this certificate pertains only to activation of this certificate and not actual travel. You must activate this certificate by theexpiration date printed on this certificate in order to receive the reservation request form. You must fill out the reservation request form with your destinationchoices and arrival dates and mail it to our fulfillment department within 6 months after activation, however travel can be completed within 12 months afteractivation. You will be required to give the travel agency multiple arrival dates and destinations. Only one 2 Night Hotel certificate Per Household Per Year. Thiscertificate has no cash surrender value, void if discontinued and where prohibited by law. The terms of this offer are subject to change without notice. Do not relyupon representations other than what is printed on this certificate or the reservation request form. CST # 3048172
  </section>

  <section class="lower">
    <div class="form-col billing">
      <h3>BILLING INFORMATION</h3>
      <div class="row"><span class="label">Name:</span><span class="line"></span></div>
      <div class="row"><span class="label">Address:</span><span class="line"></span></div>
      <div class="row"><span class="label">City:</span><span class="line"></span></div>
      <div class="row"><span class="label">State:</span><span class="line"></span></div>
      <div class="row"><span class="label">Zip Code:</span><span class="line"></span></div>
      <div class="row"><span class="label">Country:</span><span class="line"></span></div>
      <div class="row"><span class="label">Phone:</span><span class="line"></span></div>
      <div class="row"><span class="label">Email:</span><span class="line"></span></div>
      <h3 style="margin-top:12px">SHIPPING INFORMATION</h3>
      <div class="row"><span class="label">Name:</span><span class="line"></span></div>
      <div class="row"><span class="label">Address:</span><span class="line"></span></div>
      <div class="row"><span class="label">City:</span><span class="line"></span></div>
      <div class="row"><span class="label">State:</span><span class="line"></span></div>
      <div class="row"><span class="label">Zip Code:</span><span class="line"></span></div>
      <div class="row"><span class="label">Country:</span><span class="line"></span></div>
    </div>

    <div class="redeem"></div>
    <div class="redeem-notch notch-l"></div>
    <div class="redeem-notch notch-r"></div>
    <div class="redeem-inner">
      <p class="intro">Simply fill out the form on thiscertificate and enclose payment of U.S.$14.95. Vesta, MarkCard, AmeriPass, Discovery Pay, Debit Card, CheckCard, Check &amp; Money Orders are allaccepted.</p>
      <h4>3 WAYS TO REDEEM:</h4>
      <p class="step">1. For expedited redemption go to:</p>
      <p class="link">www.StayPerksOnline.com</p>
      <p class="step">2. Fax* certificate to: 1-888-555-0142</p>
      <p class="step" style="margin-top:8px">3. Mail* to:</p>
      <p class="addr">Redemption Center<br>4120 Harbor Crest Ave Ste B #210<br>Lake Verde, Ca 90000</p>
      <p class="ids">CERTIFICATE ID: &nbsp;&nbsp;&nbsp;-10002<br>EXPIRATION DATE: <span class="exp">04/08/2017</span></p>
    </div>

    <div class="form-col payment">
      <h3>PAYMENT INFORMATION</h3>
      <div class="row" style="height:12px"><span class="label">Payment Method:</span></div>
      <div class="methods">
        <span><i></i>Check</span><span><i></i>Money Order</span>
        <span><i></i>Vesta</span><span><i></i>MarkCard</span>
        <span><i></i>AMPS</span><span><i></i>Discovery Pay</span>
      </div>
      <div class="row"><span class="label">Name On Card:</span><span class="line"></span></div>
      <div class="row"><span class="label">Card # (16 digits):</span><span class="line"></span></div>
      <div class="row exp-row"><span class="label">Expiration Date:</span><span class="slot"></span>/<span class="slot2"></span></div>
      <div class="row"><span class="label">CV2#**:</span><span class="line" style="width:54px;margin-left:10px"></span></div>
      <p class="agree">I agree to terms and conditions</p>
      <div class="row"><span class="label">Signature:</span><span class="line" style="width:172px"></span></div>
      <div class="notes">
        <p>*Redemption Center" will appear on your billing statement.</p>
        <p>Make checks and money orders payable to:<br>"Redemption Center"<br>* You will receive your information by mail within 10 days.</p>
        <p>** Last 3 digits on back of card (4 digits on front of AmeriPass).</p>
      </div>
      <p class="code">2NIL -10002</p>
    </div>
  </section>
</main>
</body>
</html>
```